Cleaners Needs Bounce-Back Coupon For Laundry Service

We need a "bounce-back" coupon to attach to peoples dry cleaning orders that offers one free wash-n-fold laundry service. Right now we always attach their receipt to the bag that contains their dry cleaning when we return it. We'd like to also attach a coupon that will entice them to come try our laundry service.

Background on the service: We sort, wash, dry, and fold the laundry for customers and then neatly put it in a nice bag that makes returning very convenient. Their laundry comes out fresh, clean, smelling great, and without the hassle of doing it themselves. We have a great return rate. Most customers that try out the service become long term customers. The goal is to get our dry cleaning customers to come try it out.

Requirements:
* 5" x 8" and one-sided.
* To be printed on a standard color of card stock.
* Must incorporate our logo.
* Needs a place for us to fill in an expiration date. We'll fill in a date about two weeks out from the time they pick up their dry cleaning.
* Limit one coupon per customer.
* Limit 50 pounds of laundry per coupon.

```html
<!DOCTYPE html>
<html lang="en">
<head>
<meta charset="UTF-8">
<title>Suds on Elm – Free Wash-n-Fold Coupon</title>
<link rel="stylesheet" href="https://fonts.googleapis.com/css2?family=Oswald:wght@500&family=Arimo:wght@400;700&display=swap">
<style>
  :root {
    --navy: #0f2f7a;
    --blue: #1f4fb3;
    --sky: #8fb4ec;
    --pale: #eef4fd;
    --orange: #ec6a12;
    --white: #ffffff;
    --ink: #1a1a1a;
  }
  * { margin: 0; padding: 0; box-sizing: border-box; }
  html, body { width: 750px; height: 1200px; overflow: hidden; }
  body { font-family: "Arimo", Arial, sans-serif; background: var(--white); }

  .coupon {
    position: relative;
    width: 750px;
    height: 1200px;
    overflow: hidden;
    background: linear-gradient(180deg, var(--white) 0%, var(--pale) 45%, var(--sky) 70%, var(--blue) 100%);
  }
  .corner-accent { position: absolute; left: 0; top: 0; }

  .brand {
    position: absolute;
    left: 150px; top: 45px;
    width: 500px; height: 150px;
    display: flex; align-items: center; gap: 24px;
    padding: 0 30px;
    background: var(--white);
    border: 4px solid var(--blue);
    border-radius: 18px;
  }
  .brand-mark { width: 50px; height: 50px; background: var(--orange); border-radius: 6px; flex: none; }
  .brand-name {
    font-weight: 700; font-size: 56px; color: var(--navy);
    white-space: nowrap; line-height: 1;
  }

  .headline {
    position: absolute; left: 0; right: 0; top: 268px;
    text-align: center;
    font-family: "Oswald", "Arial Narrow", sans-serif;
    font-weight: 500;
    line-height: 1.06;
    color: var(--navy);
  }
  .headline .offer { font-size: 104px; }
  .headline .service-name { font-size: 82px; color: var(--orange); letter-spacing: 1px; }
  .headline .service-type { font-size: 84px; }

  .service-band {
    position: absolute; left: 0; right: 0; top: 592px; height: 178px;
    background: var(--orange);
    display: flex; align-items: center; justify-content: center;
    padding: 0 40px;
    color: var(--white);
    font-size: 31px;
    line-height: 1.3;
    text-align: center;
  }

  .photo-area {
    position: absolute; left: 0; top: 790px;
    width: 380px; height: 410px;
    background: linear-gradient(160deg, #dfe7f5 0%, #b9c9e6 50%, #3c5fa8 100%);
  }

  .limits-badge {
    position: absolute; left: 428px; top: 745px;
    width: 306px; height: 306px;
    border-radius: 50%;
    background: var(--navy);
    color: var(--white);
    display: flex; flex-direction: column; align-items: center; justify-content: center;
    text-align: center;
    font-size: 27px; line-height: 1.2;
  }
  .limits-badge .rule { width: 200px; height: 2px; background: var(--white); margin: 14px 0; }

  .expiry {
    position: absolute; left: 350px; top: 1062px;
    width: 375px; height: 56px;
    background: var(--white);
    border-radius: 10px;
    padding: 0 18px;
    display: flex; align-items: center;
    font-size: 30px; color: var(--ink);
  }
</style>
</head>
<body>
  <main class="coupon">
    <svg class="corner-accent" width="200" height="200" viewBox="0 0 200 200" aria-hidden="true">
      <path d="M0 0 H150 Q60 20 0 150 Z" fill="var(--blue)" opacity="0.85"/>
    </svg>

    <div class="brand">
      <span class="brand-mark"></span>
      <span class="brand-name">Suds on Elm</span>
    </div>

    <h1 class="headline">
      <span class="offer">ONE FREE</span><br>
      <span class="service-name">WASH–N–FOLD</span><br>
      <span class="service-type">LAUNDRY SERVICE</span>
    </h1>

    <p class="service-band">We sort, wash, dry, and fold the laundry for customers and then neatly put it in a nice bag that makes returning very convenient.</p>

    <div class="photo-area" role="img" aria-label="Photo of a smiling woman loading a front-loading washing machine with folded laundry"></div>

    <div class="limits-badge">
      <p>Limit<br>one coupon<br>per customer</p>
      <span class="rule"></span>
      <p>Limit 50 pounds<br>of laundry<br>per coupon</p>
    </div>

    <div class="expiry">Ex. date :</div>
  </main>
</body>
</html>
```